Redesign Power Point Template

we would like to update our powerpoint template. The current design limits the available space. we would like to keep the same colors and logo but have more room for content. We need both standard and cover template. I have attached our current template. we do not want to include the tag line "change your perspective" or the graph.

```html
<!DOCTYPE html>
<html lang="en">
<head>
<meta charset="utf-8">
<title>Lumora Presentation Template</title>
<link rel="stylesheet" href="https://fonts.googleapis.com/css2?family=Open+Sans:wght@400;600;700;800&display=swap">
<style>
:root{
  --green:#5c9b3d;
  --green-light:#8cc06b;
  --green-pale:#b9d9a3;
  --dark:#1c1c1c;
  --dark-2:#3a3a3a;
  --grey:#9a9a9a;
  --grey-light:#e9e9e9;
  --white:#ffffff;
  --canvas:#ffffff;
}
*{margin:0;padding:0;box-sizing:border-box}
html,body{width:807px;height:1200px;overflow:hidden;background:var(--canvas);font-family:"Open Sans",Arial,sans-serif;color:var(--dark)}
.board{position:relative;width:807px;height:1200px}
.slide{position:absolute;width:259px;height:197px;overflow:hidden;background:var(--white);box-shadow:0 0 3px rgba(0,0,0,.12)}
.c1{left:5px}.c2{left:274px}.c3{left:543px}
.r1{top:2px}.r2{top:202px}.r3{top:402px}.r4{top:602px}.r5{top:802px}.r6{top:1002px}

.brand{position:absolute;font-weight:800;color:var(--dark);display:flex;align-items:center;gap:3px;line-height:1}
.brand::before{content:"";display:block;background:var(--green)}
.brand-lg{left:18px;top:13px;font-size:17px}
.brand-lg::before{width:9px;height:9px}
.brand-tag{position:absolute;left:30px;top:32px;font-size:3px;font-weight:700;color:var(--dark);line-height:1}

.cover-band{position:absolute;left:0;top:44px;width:259px;height:153px}
.band-green{background:linear-gradient(110deg,#4f8d33 0%,#5c9b3d 45%,#2f4a22 70%,#6aa848 100%)}
.band-dark{background:linear-gradient(110deg,#2a2a2a 0%,#1c1c1c 45%,#3d5c2c 72%,#6aa848 100%)}
.band-light{background:linear-gradient(110deg,#f4f4f4 0%,#ececec 50%,#1f1f1f 68%,#6aa848 100%)}
.cover-title{position:absolute;left:12px;top:81px;font-size:13px;font-weight:600;color:var(--white);line-height:1}
.cover-sub{position:absolute;left:12px;top:96px;font-size:6px;color:var(--white);line-height:1}
.cover-url{position:absolute;left:12px;top:178px;font-size:4px;color:var(--white);line-height:1}
.on-light .cover-title{top:72px;color:var(--dark)}
.on-light .cover-sub{top:87px;color:var(--dark)}
.on-light .cover-url{color:var(--dark)}

.title{position:absolute;left:13px;top:12px;font-size:10px;font-weight:700;line-height:1}
.title::after{content:"";display:block;width:14px;height:1.5px;background:var(--green);margin-top:4px}
.title.plain::after{display:none}
.title.light{color:var(--white)}
.title.light::after{background:var(--white)}

.footer{position:absolute;left:0;bottom:0;width:259px;height:14px}
.footer .brand{left:5px;top:2px;font-size:9px}
.footer .brand::before{width:5px;height:5px}
.footer svg{position:absolute;left:0;top:0}
.footer .legal{position:absolute;right:12px;top:5px;font-size:2.6px;color:var(--white);line-height:1}
.footer .page{position:absolute;right:5px;top:5px;font-size:2.6px;color:var(--white);line-height:1}

.tiny{font-size:2.8px;line-height:1.35;color:var(--grey)}
.tiny.w{color:var(--white)}
.tiny.g{color:var(--green)}
.lead{font-size:4.8px;line-height:1.35;color:var(--green)}
.abs{position:absolute}
.photo{position:absolute}
.ph-city{background:linear-gradient(160deg,#dfe8ef 0%,#7fa2c0 40%,#2e4d73 100%)}
.ph-sky{background:linear-gradient(170deg,#cfdce9 0%,#6b8fb3 55%,#1f3656 100%)}
.ph-green{background:linear-gradient(120deg,#5c9b3d 0%,#7fb65e 50%,#4a8430 100%)}

.dot{position:absolute;border-radius:50%;display:flex;align-items:center;justify-content:center}
.dot svg{display:block}
.agenda-item .name{font-size:4px;color:var(--dark);line-height:1;margin-bottom:2px}
.agenda-item .name.g{color:var(--green)}
.card{position:absolute;top:58px;width:44px;height:80px;border:0.6px solid #cfcfcf;background:var(--white)}
.card-h{font-size:2.4px;font-weight:700;text-align:center;margin-top:20px;line-height:1.3;color:var(--dark)}
.card-h.g{color:var(--green)}
.card ul{list-style:disc;padding-left:8px;margin-top:5px;font-size:2.4px;color:var(--grey);line-height:1.4}
.stat-num{position:absolute;font-size:7px;text-align:center;width:50px;line-height:1}
.stat-lbl{position:absolute;font-size:2.6px;text-align:center;width:50px;color:var(--grey);line-height:1}
.stat-txt{position:absolute;font-size:2.6px;text-align:center;width:40px;color:var(--grey);line-height:1.35}
</style>
</head>
<body>
<main class="board">

<!-- Cover: green -->
<section class="slide c1 r1">
  <div class="brand brand-lg">Lumora</div><div class="brand-tag">health plan partners</div>
  <div class="cover-band band-green" role="img" aria-label="Green-tinted upward view of a glass building with window grid"></div>
  <h1 class="cover-title">Presentation Title Here</h1>
  <p class="cover-sub">Subtitle Here</p>
  <p class="cover-url">www.lumorahealth.com</p>
</section>

<!-- Cover: dark -->
<section class="slide c2 r1">
  <div class="brand brand-lg">Lumora</div><div class="brand-tag">health plan partners</div>
  <div class="cover-band band-dark" role="img" aria-label="Dark-toned upward view of a glass building with green window panes"></div>
  <h1 class="cover-title">Presentation Title Here</h1>
  <p class="cover-sub">Subtitle Here</p>
  <p class="cover-url">www.lumorahealth.com</p>
</section>

<!-- Cover: light -->
<section class="slide c3 r1 on-light">
  <div class="brand brand-lg">Lumora</div><div class="brand-tag">health plan partners</div>
  <div class="cover-band band-light" role="img" aria-label="Light grey background with a dark and green building window grid on the right"></div>
  <h1 class="cover-title">Presentation Title Here</h1>
  <p class="cover-sub">Subtitle Here</p>
  <p class="cover-url">www.lumorahealth.com</p>
</section>

<!-- Agenda -->
<section class="slide c1 r2">
  <h2 class="title plain" style="font-size:8px;font-weight:400">• Our Agenda</h2>
  <div class="agenda-item abs" style="left:35px;top:48px">
    <div class="dot" style="left:-14px;top:0;width:9px;height:9px;background:var(--green)"><svg width="5" height="5" viewBox="0 0 10 10"><circle cx="5" cy="5" r="4" fill="none" stroke="#fff" stroke-width="1.3"/><path d="M5 2.5V5h2" stroke="#fff" stroke-width="1.2" fill="none"/></svg></div>
    <p class="name g">Agenda One</p><p class="tiny">12:00<br>Short note on this first item of<br>the day and its main point.</p>
  </div>
  <div class="agenda-item abs" style="left:35px;top:92px">
    <div class="dot" style="left:-14px;top:0;width:9px;height:9px;background:var(--dark)"><svg width="5" height="5" viewBox="0 0 10 10"><circle cx="5" cy="5" r="4" fill="none" stroke="#fff" stroke-width="1.3"/><path d="M5 2.5V5h2" stroke="#fff" stroke-width="1.2" fill="none"/></svg></div>
    <p class="name">Agenda Two</p><p class="tiny">13:00<br>Short note on this second item<br>of the day and its main point.</p>
  </div>
  <div class="agenda-item abs" style="left:35px;top:132px">
    <div class="dot" style="left:-14px;top:0;width:9px;height:9px;background:var(--dark)"><svg width="5" height="5" viewBox="0 0 10 10"><circle cx="5" cy="5" r="4" fill="none" stroke="#fff" stroke-width="1.3"/><path d="M5 2.5V5h2" stroke="#fff" stroke-width="1.2" fill="none"/></svg></div>
    <p class="name">Agenda Three</p><p class="tiny">14:00<br>Short note on this third item<br>of the day and its main point.</p>
  </div>
  <div class="agenda-item abs" style="left:165px;top:46px">
    <div class="dot" style="left:-14px;top:0;width:9px;height:9px;background:var(--dark)"><svg width="5" height="5" viewBox="0 0 10 10"><circle cx="5" cy="5" r="4" fill="none" stroke="#fff" stroke-width="1.3"/><path d="M5 2.5V5h2" stroke="#fff" stroke-width="1.2" fill="none"/></svg></div>
    <p class="name">Agenda Four</p><p class="tiny">15:00<br>Short note on this fourth item<br>of the day and its main point.</p>
  </div>
  <div class="agenda-item abs" style="left:165px;top:88px">
    <div class="dot" style="left:-14px;top:0;width:9px;height:9px;background:var(--dark)"><svg width="5" height="5" viewBox="0 0 10 10"><circle cx="5" cy="5" r="4" fill="none" stroke="#fff" stroke-width="1.3"/><path d="M5 2.5V5h2" stroke="#fff" stroke-width="1.2" fill="none"/></svg></div>
    <p class="name">Agenda Five</p><p class="tiny">16:00<br>Short note on this fifth item<br>of the day and its main point.</p>
  </div>
  <div class="agenda-item abs" style="left:165px;top:130px">
    <div class="dot" style="left:-14px;top:0;width:9px;height:9px;background:var(--green)"><svg width="5" height="5" viewBox="0 0 10 10"><circle cx="5" cy="5" r="4" fill="none" stroke="#fff" stroke-width="1.3"/><path d="M5 2.5V5h2" stroke="#fff" stroke-width="1.2" fill="none"/></svg></div>
    <p class="name g">Agenda Six</p><p class="tiny">17:00<br>Short note on this sixth item<br>of the day and its main point.</p>
  </div>
  <footer class="footer"><svg width="259" height="14"><polygon points="52,4 259,4 259,14 45,14" fill="var(--green)"/></svg><div class="brand">Lumora</div><span class="legal">© 2024 Lumora. All rights reserved</span><span class="page">4</span></footer>
</section>

<!-- Title and image + text -->
<section class="slide c2 r2">
  <h2 class="title">Title And Image + Text</h2>
  <div class="abs" style="left:13px;top:39px;width:117px;height:70px;background:var(--green);padding:15px 10px">
    <p class="tiny w">Sample copy sits here to show how a short block of body text reads inside this green panel. Keep it brief and clear for every reader.</p>
    <p class="tiny w" style="margin-top:3px">Add a second line of supporting detail here.</p>
  </div>
  <div class="photo ph-city" style="left:130px;top:39px;width:117px;height:70px" role="img" aria-label="Two business people shaking hands by a city waterfront"></div>
  <p class="abs lead" style="left:13px;top:126px;width:105px">Sample lead text to open this section with a clear and friendly line of copy for readers.</p>
  <p class="abs tiny" style="left:130px;top:126px;width:117px">Supporting copy goes here to add detail on the topic above. Keep lines short and easy to read across the slide.</p>
  <p class="abs tiny" style="left:130px;top:142px;width:117px">Another short note can follow with a final point for the team.</p>
  <footer class="footer"><svg width="259" height="14"><polygon points="52,4 259,4 259,14 45,14" fill="var(--green)"/></svg><div class="brand">Lumora</div><span class="legal">© 2024 Lumora. All rights reserved</span><span class="page">5</span></footer>
</section>

<!-- Icon slide -->
<section class="slide c3 r2">
  <div class="photo ph-green" style="left:134px;top:0;width:125px;height:183px" role="img" aria-label="Green-tinted office tower photo"></div>
  <h2 class="title plain" style="left:3px;top:12px;font-size:12.5px;font-weight:400">Icon Slide</h2>
  <div class="dot" style="left:27px;top:36px;width:16px;height:16px;background:var(--dark)"><svg width="8" height="8" viewBox="0 0 10 10"><rect x="1" y="2" width="8" height="6" rx="1" fill="none" stroke="#fff"/><path d="M1 4h8" stroke="#fff"/></svg></div>
  <div class="abs" style="left:50px;top:36px;width:60px"><p class="tiny" style="color:var(--dark);font-weight:700">STRATEGY</p><p class="tiny">Short note on this point, with a line of detail here.</p></div>
  <div class="dot" style="left:27px;top:95px;width:16px;height:16px;background:var(--dark);color:#fff;font-size:8px;font-weight:700">$</div>
  <div class="abs" style="left:50px;top:95px;width:60px"><p class="tiny" style="color:var(--dark);font-weight:700">MARKETING</p><p class="tiny">Short note on this point, with a line of detail here.</p></div>
  <div class="dot" style="left:27px;top:151px;width:16px;height:16px;background:var(--dark)"><svg width="8" height="8" viewBox="0 0 10 10"><circle cx="5" cy="5" r="3.5" fill="none" stroke="#fff"/><circle cx="5" cy="5" r="1" fill="#fff"/></svg></div>
  <div class="abs" style="left:50px;top:151px;width:60px"><p class="tiny" style="color:var(--dark);font-weight:700">MARKETING</p><p class="tiny">Short note on this point, with a line of detail here.</p></div>
  <div class="dot" style="left:153px;top:36px;width:16px;height:16px;border:0.8px solid #fff;background:rgba(0,0,0,.15)"><svg width="8" height="8" viewBox="0 0 10 10"><rect x="1" y="2" width="8" height="6" fill="none" stroke="#fff"/></svg></div>
  <div class="abs" style="left:175px;top:36px;width:60px"><p class="tiny w" style="font-weight:700">STRATEGY</p><p class="tiny w">Short note on this point, with a line of detail here.</p></div>
  <div class="dot" style="left:153px;top:95px;width:16px;height:16px;border:0.8px solid #fff;background:rgba(0,0,0,.15)"><svg width="8" height="8" viewBox="0 0 10 10"><circle cx="5" cy="5" r="3.5" fill="none" stroke="#fff"/></svg></div>
  <div class="abs" style="left:175px;top:95px;width:60px"><p class="tiny w" style="font-weight:700">MARKETING</p><p class="tiny w">Short note on this point, with a line of detail here.</p></div>
  <div class="dot" style="left:153px;top:151px;width:16px;height:16px;border:0.8px solid #fff;background:rgba(0,0,0,.15)"><svg width="8" height="8" viewBox="0 0 10 10"><path d="M2 8h6M3 8V4M5 8V2M7 8V5" stroke="#fff"/></svg></div>
  <div class="abs" style="left:175px;top:151px;width:60px"><p class="tiny w" style="font-weight:700">STRATEGY</p><p class="tiny w">Short note on this point, with a line of detail here.</p></div>
  <footer class="footer"><svg width="259" height="14"><polygon points="52,4 259,4 259,14 45,14" fill="var(--green)"/></svg><div class="brand">Lumora</div><span class="legal">© 2024 Lumora. All rights reserved</span><span class="page">6</span></footer>
</section>

<!-- About us green -->
<section class="slide c1 r3" style="background:var(--green)">
  <h2 class="title light">About Us</h2>
  <div class="photo" style="left:99px;top:41px;width:61px;height:61px;border-radius:50%;background:radial-gradient(circle at 50% 40%,#e8e2dc 0%,#c9bfb5 55%,#8a8f95 100%)" role="img" aria-label="Round portrait photo of a team member"></div>
  <p class="abs tiny w" style="left:20px;top:118px;width:220px;text-align:center">Sample copy sits here to tell readers who we are, what we do and why our team cares about the people we serve every day across the region.</p>
  <p class="abs tiny w" style="left:20px;top:129px;width:220px;text-align:center">A second short line adds detail on our values, our service and the results we bring to each client.</p>
  <div class="dot" style="left:115px;top:158px;width:7px;height:7px;background:#fff"></div>
  <div class="dot" style="left:126px;top:158px;width:7px;height:7px;background:#fff"></div>
  <div class="dot" style="left:137px;top:158px;width:7px;height:7px;background:#fff"></div>
</section>

<!-- Your title goes here -->
<section class="slide c2 r3">
  <h2 class="title">Your Title Goes Here</h2>
  <p class="abs tiny" style="left:21px;top:90px;width:60px">Sample copy sits here to support the visual on the right with a short note.</p>
  <p class="abs tiny" style="left:21px;top:112px;width:60px">Add a second small block with detail on this point for readers.</p>
  <p class="abs tiny" style="left:21px;top:133px;width:60px">A last line wraps up the idea here.</p>
  <div class="photo" style="left:94px;top:38px;width:159px;height:133px;background:linear-gradient(180deg,#2a2a2a 0%,#2a2a2a 72%,#e6e6e6 72%,#cfcfcf 100%)" role="img" aria-label="Desktop monitor showing a bridge photo"></div>
  <footer class="footer"><svg width="259" height="14"><polygon points="52,4 259,4 259,14 45,14" fill="var(--green)"/></svg><div class="brand">Lumora</div><span class="legal">© 2024 Lumora. All rights reserved</span><span class="page">8</span></footer>
</section>

<!-- Section break -->
<section class="slide c3 r3" style="background:var(--green)">
  <div class="photo" style="left:95px;top:0;width:164px;height:135px;background:radial-gradient(ellipse at 100% 0%,#1c1c1c 0%,#1c1c1c 45%,#8cc06b 60%,rgba(92,155,61,0) 75%)" role="img" aria-label="Dark window grid decoration in the corner"></div>
  <h2 class="abs" style="left:21px;top:139px;font-size:10px;font-weight:700;color:#fff;line-height:1">Section Break</h2>
  <p class="abs tiny w" style="left:21px;top:152px;width:140px">Sample copy sits here to open the next section with a short and clear line of text.</p>
</section>

<!-- Title and image + text (quote) -->
<section class="slide c1 r4">
  <h2 class="title">Title And Image + Text</h2>
  <div class="photo ph-sky" style="left:13px;top:39px;width:117px;height:70px" role="img" aria-label="Glass office towers seen from below"></div>
  <div class="abs" style="left:130px;top:39px;width:117px;height:70px;background:var(--green);padding:13px 10px 0 18px">
    <p class="tiny w" style="font-size:3.2px">“ Sample quote copy sits here to share a kind word from a client on our work and team.</p>
    <p class="tiny w" style="margin-top:4px">- Client Name -</p>
  </div>
  <p class="abs tiny" style="left:13px;top:116px;width:234px">Sample copy sits here to explain this slide in more detail. Keep each line short and easy to read so the team can follow along with ease.</p>
  <p class="abs tiny" style="left:13px;top:128px;width:234px">Add a second block of copy with a further point, a short fact or a helpful note for the group to keep in mind.</p>
  <p class="abs tiny" style="left:13px;top:140px;width:234px">A third block can close out the idea with a final thought on next steps for the project.</p>
  <footer class="footer"><svg width="259" height="14"><polygon points="52,4 259,4 259,14 45,14" fill="var(--green)"/></svg><div class="brand">Lumora</div><span class="legal">© 2024 Lumora. All rights reserved</span><span class="page">10</span></footer>
</section>

<!-- About us with panel -->
<section class="slide c2 r4">
  <div class="abs" style="left:146px;top:0;width:113px;height:183px;background:var(--green-light)"></div>
  <h2 class="title">About Us</h2>
  <div class="photo ph-city" style="left:21px;top:45px;width:109px;height:77px" role="img" aria-label="Business people meeting in a bright glass lobby"></div>
  <p class="abs tiny" style="left:21px;top:133px;width:109px">Sample copy sits here to share more on our story, our team and the care we bring to every client.</p>
  <p class="abs tiny" style="left:21px;top:148px;width:109px">A second line adds a short note on our goals for the year ahead.</p>
  <p class="abs tiny w" style="left:165px;top:73px;width:60px">Sample copy sits here to add a note on who we are and what we offer, set in a short block for the reader.</p>
  <footer class="footer"><svg width="259" height="14"><polygon points="52,4 259,4 259,14 45,14" fill="var(--green)"/></svg><div class="brand">Lumora</div><span class="legal">© 2024 Lumora. All rights reserved</span><span class="page">11</span></footer>
</section>

<!-- Three bullets -->
<section class="slide c3 r4">
  <h2 class="title">Three Bullets Area</h2>
  <div class="photo ph-sky" style="left:0;top:39px;width:259px;height:76px" role="img" aria-label="Blue glass office tower against the sky"></div>
  <div class="dot" style="left:33px;top:104px;width:30px;height:30px;background:var(--green)"><svg width="14" height="14" viewBox="0 0 14 14"><circle cx="3" cy="7" r="1.8" fill="none" stroke="#fff"/><circle cx="11" cy="3" r="1.8" fill="none" stroke="#fff"/><circle cx="11" cy="11" r="1.8" fill="none" stroke="#fff"/><path d="M4.6 6.2L9.4 3.8M4.6 7.8L9.4 10.2" stroke="#fff"/></svg></div>
  <div class="dot" style="left:114px;top:104px;width:30px;height:30px;background:var(--dark)"><svg width="14" height="14" viewBox="0 0 14 14"><path d="M7 2L12 4.5 7 7 2 4.5Z M2 7l5 2.5 5-2.5 M2 9.5l5 2.5 5-2.5" fill="none" stroke="#fff"/></svg></div>
  <div class="dot" style="left:196px;top:104px;width:30px;height:30px;background:var(--dark-2)"><svg width="14" height="14" viewBox="0 0 14 14"><path d="M4 12h6l-1-3c2-1 2-4 0-5L7 2 5 4c-1 1-1 3 0 4z" fill="#fff"/></svg></div>
  <p class="abs tiny" style="left:20px;top:140px;width:56px;text-align:center">Short note here on the first point made.</p>
  <p class="abs tiny" style="left:101px;top:140px;width:56px;text-align:center">Short note here on the second point made.</p>
  <p class="abs tiny" style="left:183px;top:140px;width:56px;text-align:center">Short note here on the third point made.</p>
  <footer class="footer"><svg width="259" height="14"><polygon points="52,4 259,4 259,14 45,14" fill="var(--green)"/></svg><div class="brand">Lumora</div><span class="legal">© 2024 Lumora. All rights reserved</span><span class="page">12</span></footer>
</section>

<!-- Four column -->
<section class="slide c1 r5">
  <h2 class="title">Four Column Area</h2>
  <div class="card" style="left:18px"><p class="card-h g">EXPLORATION OF THE<br>FIRST IDEA</p><ul><li>Short point one</li><li>Short point two</li><li>Short point three</li></ul></div>
  <div class="card" style="left:78px"><p class="card-h">EXPLORATION OF THE<br>SECOND IDEA</p><ul><li>Short point one</li><li>Short point two</li><li>Short point three</li></ul></div>
  <div class="card" style="left:138px"><p class="card-h">EXPLORATION OF THE<br>THIRD IDEA</p><ul><li>Short point one</li><li>Short point two</li><li>Short point three</li></ul></div>
  <div class="card" style="left:198px"><p class="card-h g">EXPLORATION OF THE<br>FOURTH IDEA</p><ul><li>Short point one</li><li>Short point two</li><li>Short point three</li></ul></div>
  <div class="dot" style="left:32px;top:49px;width:17px;height:17px;background:var(--green)"><svg width="8" height="8" viewBox="0 0 10 10"><path d="M2 1h6v3a3 3 0 0 1-6 0zM5 7v2M3 9h4" fill="#fff" stroke="#fff"/></svg></div>
  <div class="dot" style="left:92px;top:49px;width:17px;height:17px;background:var(--dark)"><svg width="8" height="8" viewBox="0 0 10 10"><path d="M1 3l2 2 2-3 2 3 2-2-1 5H2z" fill="#fff"/></svg></div>
  <div class="dot" style="left:152px;top:49px;width:17px;height:17px;background:var(--dark-2)"><svg width="8" height="8" viewBox="0 0 10 10"><path d="M2 8l2-1 4-4 1-2-2 1-4 4z" fill="#fff"/></svg></div>
  <div class="dot" style="left:212px;top:49px;width:17px;height:17px;background:var(--green-light)"><svg width="8" height="8" viewBox="0 0 10 10"><circle cx="5" cy="4" r="3" fill="#fff"/><path d="M4 8h2" stroke="#fff"/></svg></div>
  <footer class="footer"><svg width="259" height="14"><polygon points="52,4 259,4 259,14 45,14" fill="var(--green)"/></svg><div class="brand">Lumora</div><span class="legal">© 2024 Lumora. All rights reserved</span><span class="page">13</span></footer>
</section>

<!-- Circle infographic -->
<section class="slide c2 r5">
  <h2 class="title">Circle Infographic</h2>
  <svg class="abs" style="left:78px;top:49px" width="104" height="104" viewBox="-52 -52 104 104">
    <g stroke="#fff" stroke-width="1.5">
      <path d="M0-50A50 50 0 0 1 35.4-35.4L19.8-19.8A28 28 0 0 0 0-28Z" fill="var(--dark)"/>
      <path d="M35.4-35.4A50 50 0 0 1 50 0L28 0A28 28 0 0 0 19.8-19.8Z" fill="var(--green-light)"/>
      <path d="M50 0A50 50 0 0 1 35.4 35.4L19.8 19.8A28 28 0 0 0 28 0Z" fill="var(--green)"/>
      <path d="M35.4 35.4A50 50 0 0 1 0 50L0 28A28 28 0 0 0 19.8 19.8Z" fill="var(--dark)"/>
      <path d="M0 50A50 50 0 0 1-35.4 35.4L-19.8 19.8A28 28 0 0 0 0 28Z" fill="var(--dark-2)"/>
      <path d="M-35.4 35.4A50 50 0 0 1-50 0L-28 0A28 28 0 0 0-19.8 19.8Z" fill="var(--green-light)"/>
      <path d="M-50 0A50 50 0 0 1-35.4-35.4L-19.8-19.8A28 28 0 0 0-28 0Z" fill="var(--green)"/>
      <path d="M-35.4-35.4A50 50 0 0 1 0-50L0-28A28 28 0 0 0-19.8-19.8Z" fill="var(--dark)"/>
    </g>
    <circle r="26" fill="#fff"/>
    <path d="M0-13L3.5-4 13-4 5.5 2 8.5 11 0 5.5-8.5 11-5.5 2-13-4-3.5-4Z" fill="none" stroke="var(--dark)" stroke-width="1.2"/>
  </svg>
  <div class="dot" style="left:54px;top:74px;width:12px;height:12px;border:0.8px solid var(--green)"></div>
  <div class="dot" style="left:54px;top:126px;width:12px;height:12px;border:0.8px solid var(--dark)"></div>
  <div class="dot" style="left:194px;top:74px;width:12px;height:12px;background:var(--dark)"></div>
  <div class="dot" style="left:194px;top:126px;width:12px;height:12px;border:0.8px solid var(--green)"></div>
  <div class="abs" style="left:14px;top:71px;width:36px;text-align:right"><p class="tiny g">Secure</p><p class="tiny">Short note on this point.</p></div>
  <div class="abs" style="left:14px;top:123px;width:36px;text-align:right"><p class="tiny">Good Package</p><p class="tiny">Short note on this point.</p></div>
  <div class="abs" style="left:210px;top:71px;width:40px"><p class="tiny" style="color:var(--dark)">Well Organized</p><p class="tiny">Short note on this point.</p></div>
  <div class="abs" style="left:210px;top:123px;width:40px"><p class="tiny g">Publication</p><p class="tiny">Short note on this point.</p></div>
  <footer class="footer"><svg width="259" height="14"><polygon points="52,4 259,4 259,14 45,14" fill="var(--green)"/></svg><div class="brand">Lumora</div><span class="legal">© 2024 Lumora. All rights reserved</span><span class="page">14</span></footer>
</section>

<!-- Chart -->
<section class="slide c3 r5">
  <h2 class="title">Chart Title</h2>
  <svg class="abs" style="left:0;top:50px" width="259" height="40" viewBox="0 0 259 40">
    <g fill="none" stroke-width="2.5">
      <circle cx="45" cy="20" r="16" stroke="var(--grey-light)"/>
      <circle cx="45" cy="20" r="16" stroke="var(--green)" stroke-dasharray="60.3 100.5" transform="rotate(-90 45 20)"/>
      <circle cx="101" cy="20" r="16" stroke="var(--grey-light)"/>
      <circle cx="101" cy="20" r="16" stroke="var(--dark)" stroke-dasharray="25.1 100.5" transform="rotate(-90 101 20)"/>
      <circle cx="157" cy="20" r="16" stroke="var(--grey-light)"/>
      <circle cx="157" cy="20" r="16" stroke="var(--dark-2)" stroke-dasharray="45.2 100.5" transform="rotate(-90 157 20)"/>
      <circle cx="214" cy="20" r="16" stroke="var(--grey-light)"/>
      <circle cx="214" cy="20" r="16" stroke="var(--green-light)" stroke-dasharray="15.1 100.5" transform="rotate(-90 214 20)"/>
    </g>
    <circle cx="45" cy="20" r="10" fill="var(--green)"/><text x="45" y="22" font-size="5" fill="#fff" text-anchor="middle" font-family="Open Sans, sans-serif">60%</text>
    <circle cx="101" cy="20" r="10" fill="var(--dark)"/><text x="101" y="22" font-size="5" fill="#fff" text-anchor="middle" font-family="Open Sans, sans-serif">25%</text>
    <circle cx="157" cy="20" r="10" fill="var(--dark-2)"/><text x="157" y="22" font-size="5" fill="#fff" text-anchor="middle" font-family="Open Sans, sans-serif">45%</text>
    <circle cx="214" cy="20" r="10" fill="var(--green-light)"/><text x="214" y="22" font-size="5" fill="#fff" text-anchor="middle" font-family="Open Sans, sans-serif">15%</text>
  </svg>
  <p class="stat-num" style="left:20px;top:97px;color:var(--green)">89,750</p>
  <p class="stat-num" style="left:76px;top:97px">120,890</p>
  <p class="stat-num" style="left:132px;top:97px">2,508</p>
  <p class="stat-num" style="left:189px;top:97px;color:var(--green-light)">75,600</p>
  <p class="stat-lbl" style="left:20px;top:109px">Growing Company</p>
  <p class="stat-lbl" style="left:76px;top:109px">Success Chart</p>
  <p class="stat-lbl" style="left:132px;top:109px">Subscribers</p>
  <p class="stat-lbl" style="left:189px;top:109px">Happy Business</p>
  <p class="stat-txt" style="left:25px;top:116px">Short note on this figure and what it shows for the year.</p>
  <p class="stat-txt" style="left:81px;top:116px">Short note on this figure and what it shows for the year.</p>
  <p class="stat-txt" style="left:137px;top:116px">Short note on this figure and what it shows for the year.</p>
  <p class="stat-txt" style="left:194px;top:116px">Short note on this figure and what it shows for the year.</p>
  <footer class="footer"><svg width="259" height="14"><polygon points="52,4 259,4 259,14 45,14" fill="var(--green)"/></svg><div class="brand">Lumora</div><span class="legal">© 2024 Lumora. All rights reserved</span><span class="page">15</span></footer>
</section>

<!-- Thank you -->
<section class="slide c2 r6">
  <div class="brand brand-lg">Lumora</div><div class="brand-tag">health plan partners</div>
  <div class="cover-band band-dark" role="img" aria-label="Dark upward view of a glass building"></div>
  <h1 class="abs" style="left:17px;top:106px;font-size:23px;font-weight:700;color:#fff;line-height:1">Thank You</h1>
  <p class="abs" style="left:22px;top:136px;font-size:5.5px;color:#fff;line-height:1">John Doe</p>
  <p class="abs tiny w" style="left:22px;top:145px">☏ 000-0000-0000<br>✉ info@youremail.com<br>⌂ Your Street name 12, Your City 12345</p>
</section>

</main>
</body>
</html>
```